Increased budget: GUI redesign: 10 year old user interface needs modern look-and-feel

UPDATE: Please DO look at more than only th eone image I attached! Almost all designs are simply reworks of that one picture. That is not what we are looking for. Check out the video to understand what the product does, and try to make something better.
We have an existing app (see https://www.vextorane.com/downloadBrivoPanel.php?vers=3_9_1_140964&dir=Vextorane_OEM/3_9_1_140964&name=DSP_Control_Software) which needs refreshing. See also a video here: https://vextorane-oem.com/software/ and the user manual attached here. The GUI is now 800x400 pixels, which is too small; and not scalable, which will be fixed in the future. We need a new, modern look-and-feel, and images that can be exported from the design in various sizes. The current design is attached as well as a collection of PNG files. The overall layout can stay similar, although we are open to good ideas for improvements. The design should be targeted at professional users, not end users; the product is used by audio professionals (e.g. sound engineers, loudspeaker designers). Also see our web version: https://www.vextorane.com/brivopanel/skins/1_1_2/container.html?MAC=Demo%201x2
The winner will also be asked to do a full design of the application GUI (based on the design done here), with several more windows etc, and additional payment depending on the work to be done.

Target Market(s)

Professional audio

Industry/Entity Type

Audio / Industrial

Font styles to use
Other font styles liked:
• Futura (not mandatory)

Colors

Designer to choose colors to be used in the design.

Requirements
Must have
• Modern, timeless design, not too bling bling
Nice to have
• Flat design
Should not have
• 3D, bling bling, many colours, etc

```html
<!DOCTYPE html>
<html lang="en">
<head>
<meta charset="utf-8">
<title>Vextorane – Cross-Over</title>
<link href="https://fonts.googleapis.com/css2?family=Jost:wght@400;500;600;700&display=swap" rel="stylesheet">
<style>
  :root{
    --bg:#1f1f1f;
    --frame:#252525;
    --panel:#2a2a2a;
    --black:#000;
    --ctrl:#363636;
    --ctrl-line:#4a4a4a;
    --grid:#5a5a5a;
    --text:#ffffff;
    --muted:#cfcfcf;
    --label:#bdbdbd;
    --accent:#ee8a0c;
    --accent-dark:#d97400;
    --led-on:#7bd83c;
    --led-off:#3b3b3b;
  }
  *{box-sizing:border-box;margin:0;padding:0}
  html,body{width:1200px;height:1200px;overflow:hidden;background:var(--bg);font-family:"Jost",sans-serif;color:var(--text)}
  .app{position:absolute;left:60px;top:310px;width:1080px;height:579px;background:var(--frame);border-radius:12px}
  .sidebar{position:absolute;left:10px;top:10px;width:139px;height:560px;background:var(--panel);border-radius:8px}
  .workspace{position:absolute;left:154px;top:10px;width:916px;height:560px;background:var(--panel);border-radius:8px}

  .brand{position:absolute;left:0;top:24px;width:139px;text-align:center}
  .brand-mark{width:12px;height:12px;background:var(--accent);margin:0 auto 6px}
  .brand-name{font-size:13px;font-weight:500;letter-spacing:.5px;color:var(--text)}

  .nav-btn{position:absolute;left:10px;width:119px;height:29px;background:var(--black);border-radius:4px;
    font-size:8px;font-weight:500;display:flex;align-items:center;justify-content:center}
  .nav-btn.active{background:var(--accent);font-weight:600}

  .graph{position:absolute;left:230px;top:335px;width:700px;height:260px;background:var(--black);border-radius:8px}
  .graph svg{position:absolute;left:0;top:0}
  .tool{position:absolute;left:10px;width:14px;height:14px;background:#262626;border-radius:2px}
  .axis-y,.axis-x{position:absolute;font-size:9.5px;color:var(--muted)}

  .meters-title{position:absolute;left:951px;top:334px;font-size:9px;color:var(--muted)}
  .meter-label{position:absolute;font-size:6px;color:var(--muted);width:14px;text-align:center}
  .meter-bar{position:absolute;top:356px;width:10px;height:121px;background:var(--black)}
  .rule{position:absolute;left:951px;width:159px;height:1px;background:#3e3e3e}
  .phase-title{position:absolute;left:951px;top:565px;font-size:7.5px;color:var(--muted)}
  .led{position:absolute;top:577px;width:14px;height:14px;border-radius:50%;background:var(--led-off)}
  .led.on{background:var(--led-on)}

  .section-title{position:absolute;left:230px;top:605px;font-size:17px;font-weight:700;color:#d9d9d9;letter-spacing:.3px}
  .section-rule{position:absolute;left:327px;top:618px;width:788px;height:1px;background:#6a6a6a}
  .ch-num{position:absolute;top:640px;width:139px;text-align:center;font-size:16px;font-weight:700;color:#d9d9d9}
  .row-letter{position:absolute;left:230px;font-size:11px;font-weight:700;color:#d9d9d9;width:10px;text-align:center}

  .ctrl{position:absolute;width:139px;height:24px;background:var(--ctrl);border:1px solid var(--ctrl-line);border-radius:3px;
    font-size:8px;display:flex;align-items:center;justify-content:center}
  .select{position:absolute;width:139px;height:28px;background:var(--black);border-radius:3px;font-size:7.5px;
    display:flex;align-items:center;justify-content:space-between;padding:0 8px}
  .select i{width:0;height:0;border-left:3.5px solid transparent;border-right:3.5px solid transparent;border-top:6px solid var(--text)}
</style>
</head>
<body>
<div class="app">
  <div class="sidebar">
    <div class="brand"><div class="brand-mark"></div><div class="brand-name">VEXTORANE</div></div>
  </div>
  <div class="workspace"></div>
</div>

<nav>
  <div class="nav-btn" style="left:80px;top:422px">Main</div>
  <div class="nav-btn active" style="left:80px;top:465px">X-over</div>
  <div class="nav-btn" style="left:80px;top:509px">In 1</div>
  <div class="nav-btn" style="left:80px;top:552px">In 2</div>
  <div class="nav-btn" style="left:80px;top:596px">In 3</div>
  <div class="nav-btn" style="left:80px;top:640px">In 4</div>
  <div class="nav-btn" style="left:80px;top:684px">Out 1</div>
  <div class="nav-btn" style="left:80px;top:727px">Out 2</div>
  <div class="nav-btn" style="left:80px;top:771px">Out 3</div>
  <div class="nav-btn" style="left:80px;top:815px">Out 4</div>
</nav>

<section class="graph">
  <svg width="700" height="260" viewBox="0 0 700 260">
    <g stroke="var(--grid)" stroke-width="0.8" fill="none">
      <rect x="33" y="16" width="624" height="208"/>
      <path d="M95.4 16V224M157.8 16V224M220.2 16V224M282.6 16V224M345 16V224M407.4 16V224M469.8 16V224M532.2 16V224M594.6 16V224"/>
      <path d="M33 50.7H657M33 85.3H657M33 120H657M33 154.7H657M33 189.3H657"/>
    </g>
    <g stroke="#bbb" stroke-width="0.8" fill="none">
      <rect x="10" y="14" width="14" height="14" rx="2" fill="#262626" stroke="none"/>
      <path d="M13 17l8 8M13 17h3M13 17v3M21 25h-3M21 25v-3"/>
      <rect x="10" y="38" width="14" height="14" rx="2" fill="#262626" stroke="none"/>
      <circle cx="16.3" cy="44.3" r="2.8"/><path d="M18.3 46.3l2.5 2.5"/>
      <rect x="10" y="62" width="14" height="14" rx="2" fill="#262626" stroke="none"/>
      <path d="M13.5 65.5h7M17 65.5v7.5M15.5 73h3"/>
    </g>
  </svg>
  <span class="axis-y" style="left:667px;top:12px">10</span>
  <span class="axis-y" style="left:667px;top:46px">0dB</span>
  <span class="axis-y" style="left:667px;top:80px">- 10</span>
  <span class="axis-y" style="left:667px;top:114px">- 20</span>
  <span class="axis-y" style="left:667px;top:148px">- 30</span>
  <span class="axis-y" style="left:667px;top:182px">- 40</span>
  <span class="axis-y" style="left:667px;top:216px">- 50</span>
  <span class="axis-x" style="left:33px;top:236px">10</span>
  <span class="axis-x" style="left:91px;top:236px">20</span>
  <span class="axis-x" style="left:152px;top:236px">50</span>
  <span class="axis-x" style="left:212px;top:236px">100</span>
  <span class="axis-x" style="left:277px;top:236px">200</span>
  <span class="axis-x" style="left:344px;top:236px">500</span>
  <span class="axis-x" style="left:409px;top:236px">1k</span>
  <span class="axis-x" style="left:466px;top:236px">2k</span>
  <span class="axis-x" style="left:525px;top:236px">5k</span>
  <span class="axis-x" style="left:583px;top:236px">10k</span>
  <span class="axis-x" style="left:647px;top:236px">20k</span>
</section>

<section class="meters">
  <div class="meters-title">Output Level</div>
  <div class="meter-bar" style="left:972px"></div>
  <div class="meter-bar" style="left:1016px"></div>
  <div class="meter-bar" style="left:1061px"></div>
  <div class="meter-bar" style="left:1105px"></div>
  <div style="position:absolute;left:949px;top:357px">
    <div class="meter-label" style="left:0;top:0">+12</div><div class="meter-label" style="left:0;top:18.5px">0</div><div class="meter-label" style="left:0;top:37px">-6</div><div class="meter-label" style="left:0;top:55.5px">-12</div><div class="meter-label" style="left:0;top:74px">-24</div><div class="meter-label" style="left:0;top:92.5px">-36</div><div class="meter-label" style="left:0;top:111px">-48</div>
    <div class="meter-label" style="left:44px;top:0">+12</div><div class="meter-label" style="left:44px;top:18.5px">0</div><div class="meter-label" style="left:44px;top:37px">-6</div><div class="meter-label" style="left:44px;top:55.5px">-12</div><div class="meter-label" style="left:44px;top:74px">-24</div><div class="meter-label" style="left:44px;top:92.5px">-36</div><div class="meter-label" style="left:44px;top:111px">-48</div>
    <div class="meter-label" style="left:89px;top:0">+12</div><div class="meter-label" style="left:89px;top:18.5px">0</div><div class="meter-label" style="left:89px;top:37px">-6</div><div class="meter-label" style="left:89px;top:55.5px">-12</div><div class="meter-label" style="left:89px;top:74px">-24</div><div class="meter-label" style="left:89px;top:92.5px">-36</div><div class="meter-label" style="left:89px;top:111px">-48</div>
    <div class="meter-label" style="left:133px;top:0">+12</div><div class="meter-label" style="left:133px;top:18.5px">0</div><div class="meter-label" style="left:133px;top:37px">-6</div><div class="meter-label" style="left:133px;top:55.5px">-12</div><div class="meter-label" style="left:133px;top:74px">-24</div><div class="meter-label" style="left:133px;top:92.5px">-36</div><div class="meter-label" style="left:133px;top:111px">-48</div>
  </div>
  <div class="rule" style="top:489px"></div>
  <div class="rule" style="top:522px"></div>
  <div class="rule" style="top:555px"></div>
  <svg style="position:absolute;left:951px;top:495px" width="160" height="55" viewBox="0 0 160 55" fill="none" stroke="#cfcfcf" stroke-width="0.9" stroke-linecap="round">
    <g transform="translate(40 11)">
      <path d="M-2 -3.5h-3a3.5 3.5 0 0 0 0 7h3M2 -3.5h3a3.5 3.5 0 0 1 0 7h-3M-3 0h6"/>
    </g>
    <g transform="translate(124 11)">
      <path d="M-2 -3.5h-3a3.5 3.5 0 0 0 0 7h3M2 -3.5h3a3.5 3.5 0 0 1 0 7h-3M-6 -6l12 12"/>
    </g>
    <g transform="translate(19 43)"><path d="M-6 -2h2l4 -3.5v11l-4 -3.5h-2z"/><path d="M2 -2a3 3 0 0 1 0 4M3.5 -4a6 6 0 0 1 0 8"/></g>
    <g transform="translate(59 43)"><path d="M-6 -2h2l4 -3.5v11l-4 -3.5h-2z"/><path d="M2.5 -1l3 3M5.5 -1l-3 3"/></g>
    <g transform="translate(99 43)"><path d="M-6 -2h2l4 -3.5v11l-4 -3.5h-2z"/><path d="M2 -2a3 3 0 0 1 0 4M3.5 -4a6 6 0 0 1 0 8"/></g>
    <g transform="translate(139 43)"><path d="M-6 -2h2l4 -3.5v11l-4 -3.5h-2z"/><path d="M2 -2a3 3 0 0 1 0 4M3.5 -4a6 6 0 0 1 0 8M-6 -6l12 12"/></g>
  </svg>
  <div class="phase-title">Phase Invert</div>
  <div class="led on" style="left:967px"></div>
  <div class="led" style="left:1004px"></div>
  <div class="led on" style="left:1041px"></div>
  <div class="led" style="left:1079px"></div>
</section>

<section class="crossover">
  <h2 class="section-title">Cross-Over</h2>
  <div class="section-rule"></div>
  <div class="row-letter" style="top:674px">H</div><div class="row-letter" style="top:689px">P</div><div class="row-letter" style="top:704px">F</div>
  <div class="row-letter" style="top:745px">L</div><div class="row-letter" style="top:760px">P</div><div class="row-letter" style="top:775px">F</div>
  <div class="row-letter" style="top:815px">G</div><div class="row-letter" style="top:830px">D</div>

  <div class="ch-num" style="left:250px">1</div>
  <div class="ctrl" style="left:250px;top:671px">Off</div>
  <div class="select" style="left:250px;top:700px">But 24dB<i></i></div>
  <div class="ctrl" style="left:250px;top:739px">Off</div>
  <div class="select" style="left:250px;top:768px">But 24dB<i></i></div>
  <div class="ctrl" style="left:250px;top:807px">0.00 dB</div>
  <div class="ctrl" style="left:250px;top:836px">0.00 ms</div>

  <div class="ch-num" style="left:409px">2</div>
  <div class="ctrl" style="left:409px;top:671px">Off</div>
  <div class="select" style="left:409px;top:700px">But 24dB<i></i></div>
  <div class="ctrl" style="left:409px;top:739px">Off</div>
  <div class="select" style="left:409px;top:768px">But 24dB<i></i></div>
  <div class="ctrl" style="left:409px;top:807px">0.00 dB</div>
  <div class="ctrl" style="left:409px;top:836px">0.00 ms</div>

  <div class="ch-num" style="left:568px">3</div>
  <div class="ctrl" style="left:568px;top:671px">Off</div>
  <div class="select" style="left:568px;top:700px">But 24dB<i></i></div>
  <div class="ctrl" style="left:568px;top:739px">Off</div>
  <div class="select" style="left:568px;top:768px">But 24dB<i></i></div>
  <div class="ctrl" style="left:568px;top:807px">0.00 dB</div>
  <div class="ctrl" style="left:568px;top:836px">0.00 ms</div>

  <div class="ch-num" style="left:727px">4</div>
  <div class="ctrl" style="left:727px;top:671px">Off</div>
  <div class="select" style="left:727px;top:700px">But 24dB<i></i></div>
  <div class="ctrl" style="left:727px;top:739px">Off</div>
  <div class="select" style="left:727px;top:768px">But 24dB<i></i></div>
  <div class="ctrl" style="left:727px;top:807px">0.00 dB</div>
  <div class="ctrl" style="left:727px;top:836px">0.00 ms</div>
</section>
</body>
</html>
```